property investment and development company needs a website

we need a website that looks professional and portrays trust for people looking to us to buy their house or investors looking to invest or joint venture with us.
We are based in the west midlands in the UK.
we deal mainly with residential housing, house to flats conversions, HMO's (houses in multiple ocupancy).
we require the website as a first point of contact with potential sellers, renters and investors so links or contact details that are easy to access or see would be good.
I have had logos designed by a plan hollow member and these can be used as guidance for the colour and style of the site.
Target Market(s)
joint venture investment partners, people looking to sell their house, people looking to rent from us.
Coding
Coded - Design and coding required
Number of Pages Required
3 page
Requirements
Must have
- project a professional appearance
- visable contact details

```html
<!DOCTYPE html>
<html lang="en">
<head>
<meta charset="utf-8">
<title>Hartwell Homes</title>
<link href="https://fonts.googleapis.com/css2?family=Tinos&family=Open+Sans:wght@400;600;700&family=Ubuntu:wght@400;500&display=swap" rel="stylesheet">
<style>
:root{
  --gold:#d2a75c;
  --gold-light:#e0bd7c;
  --gold-dark:#c4944a;
  --cream:#f3f2e6;
  --navy:#262a3a;
  --slate:#3f4d6e;
  --ink:#3a3a3a;
  --muted:#8a8a8a;
  --white:#ffffff;
}
*{margin:0;padding:0;box-sizing:border-box}
html,body{width:1200px;height:3560px;overflow:hidden}
body{font-family:"Open Sans",Arial,sans-serif;color:var(--ink);background:var(--white);position:relative}
section{position:absolute;left:0;width:1200px;overflow:hidden}
.serif{font-family:"Tinos","Times New Roman",serif;font-weight:400}

/* Hero */
.hero{top:0;height:745px}
.hero-photo{position:absolute;inset:0;background:linear-gradient(180deg,#5c6475 0%,#6c6a6a 35%,#8a6a4f 60%,#5a5c52 85%,#6e7570 100%)}
.hero-shade{position:absolute;inset:0;background:rgba(30,35,50,.25)}
.brand{position:absolute;left:74px;top:20px;color:var(--white);font-family:"Tinos",serif;font-size:26px;line-height:28px;letter-spacing:1px;display:flex;align-items:center;gap:12px}
.brand-mark{width:40px;height:40px;border:2px solid var(--gold)}
.main-nav{position:absolute;top:36px;left:0;width:1200px;font-size:15px;font-weight:700;color:var(--white)}
.main-nav a{position:absolute;color:inherit;text-decoration:none;letter-spacing:.3px}
.nav-rule{position:absolute;left:74px;top:89px;width:1049px;height:1px;background:rgba(255,255,255,.55)}
.hero-title{position:absolute;top:312px;width:1200px;text-align:center;color:var(--white);font-size:56px}
.hero-sub{position:absolute;top:382px;width:1200px;text-align:center;color:var(--white);font-size:32px}
.hero-line{position:absolute;top:436px;width:1200px;text-align:center;color:var(--white);font-size:19px}
.search-tabs{position:absolute;top:487px;left:0;width:1200px;color:var(--white);font-size:13px;font-weight:700}
.search-tabs span{position:absolute}
.search-tabs .active{border-bottom:3px solid var(--gold);padding-bottom:8px}
.search-bar{position:absolute;left:289px;top:538px;width:624px;height:50px;background:var(--white);display:flex}
.search-bar .search-btn{margin-left:auto;width:91px;height:50px;background:var(--gold)}

/* About */
.about{top:745px;height:551px;background:var(--cream)}
.section-title{position:absolute;width:1200px;text-align:center;color:var(--gold);font-size:50px}
.about-text{position:absolute;top:127px;left:340px;width:520px;text-align:center;font-size:14.5px;line-height:21px;color:#444}
.feature{position:absolute;width:300px}
.feature h3{font-weight:400;font-size:21px;color:#333;margin-bottom:14px}
.feature p{font-size:14px;line-height:21px;color:var(--muted)}
.feature.left{text-align:right}
.feature-icon{position:absolute;width:44px;height:44px}
.emblem{position:absolute;left:494px;top:218px;width:234px;height:259px;background:radial-gradient(circle,rgba(210,167,92,.28),rgba(210,167,92,.08) 70%,transparent 72%)}

/* Listings */
.listings{top:1296px;height:551px;background:var(--white)}
.listings-link{position:absolute;top:123px;width:1200px;text-align:center;font-size:15px;color:#444}
.listing{position:absolute;top:166px;width:277px}
.listing-photo{height:234px;border-radius:4px}
.listing-meta{padding:8px 14px 0;font-size:11.5px;line-height:17px;color:#333}
.listing-meta .specs span{margin-right:22px}

/* Stats */
.stats{top:1847px;height:183px;background:linear-gradient(90deg,var(--gold-dark),var(--gold-light) 50%,var(--gold-dark))}
.stat{position:absolute;top:48px;width:240px;margin-left:-120px;text-align:center;color:var(--white)}
.stat b{display:block;font-family:"Open Sans",sans-serif;font-weight:400;font-size:48px;line-height:56px}
.stat span{font-size:19px}

/* Sell / Invest */
.sell{top:2030px;height:464px;background:var(--white)}
.invest{top:2494px;height:461px;background:var(--navy)}
.feature-photo{position:absolute;top:0;height:100%;width:600px}
.sell .feature-photo{left:0;background:linear-gradient(180deg,#b97f5e 0%,#d8a37a 25%,#6f6660 55%,#4d4b48 80%,#5e6f4a 100%)}
.invest .feature-photo{left:600px;background:linear-gradient(180deg,#c9cdd3 0%,#7e8a8f 30%,#4c3a2a 55%,#c6884a 62%,#2f3438 85%,#3c4447 100%)}
.block-title{position:absolute;color:var(--gold);font-size:46px}
.block-copy{position:absolute;width:480px;font-size:14.5px;line-height:21px}
.block-copy p{margin-bottom:21px}
.sell .block-copy{color:#666}
.invest .block-copy{color:#9aa0b0}
.btn{position:absolute;width:118px;height:30px;background:var(--gold);color:var(--white);font-size:13px;line-height:30px;text-align:center;border-radius:3px}

/* Contact */
.contact{top:2955px;height:605px;background:var(--cream)}
.contact-heading{position:absolute;left:94px;top:68px;font-family:"Ubuntu",sans-serif;font-weight:500;font-size:36px;line-height:42px;color:var(--slate)}
.contact-rule{position:absolute;left:94px;top:197px;width:79px;height:3px;background:#a8a290}
.contact-region{position:absolute;left:94px;top:253px;font-family:"Ubuntu",sans-serif;font-weight:500;font-size:20px;color:#333}
.contact-address{position:absolute;left:94px;top:294px;font-size:11.5px;line-height:18px;color:#444}
.info-col{position:absolute;top:365px;font-family:"Ubuntu",sans-serif;font-size:16px;line-height:30px;color:#333}
.info-col h4{font-weight:500;font-size:19px;margin-bottom:8px}
.info-col .soft{color:var(--muted)}
.map{position:absolute;left:654px;top:32px;width:544px;height:544px;border-radius:50%;background:radial-gradient(circle at 50% 50%,#ece7df 0%,#e3ded6 60%,#d9d4cc 100%)}
</style>
</head>
<body>

<section class="hero">
  <div class="hero-photo" role="img" aria-label="Modern detached family home at dusk with lit windows and landscaped front garden"></div>
  <div class="hero-shade"></div>
  <div class="brand"><span class="brand-mark"></span><span>HARTWELL<br>HOMES</span></div>
  <nav class="main-nav">
    <a href="#" style="left:532px">BUY</a>
    <a href="#" style="left:631px">SELL</a>
    <a href="#" style="left:733px">RENT</a>
    <a href="#" style="left:838px">INVEST</a>
    <a href="#" style="left:962px">NEWS AND INSIGHTS</a>
  </nav>
  <div class="nav-rule"></div>
  <h1 class="hero-title serif">Be an Investor, a Landlord,</h1>
  <p class="hero-sub serif">and/or find your dream home</p>
  <p class="hero-line">with the most complete source of homes and real estate near you</p>
  <div class="search-tabs">
    <span class="active" style="left:410px">BUY</span>
    <span style="left:492px">RENT</span>
    <span style="left:570px">INVEST</span>
    <span style="left:676px">HOME VALUE</span>
  </div>
  <div class="search-bar"><div class="search-btn"></div></div>
</section>

<section class="about">
  <h2 class="section-title serif" style="top:55px">About Us</h2>
  <p class="about-text">We are a property development and investment company that have our own portfolio and we are active investors who pride ourselves in expanding our business organically.</p>

  <div class="feature left" style="left:26px;top:255px">
    <h3>Data Driven</h3>
    <p>In-depth information on cities,<br>renters and neighborhoods</p>
  </div>
  <svg class="feature-icon" style="left:350px;top:253px" viewBox="0 0 44 44" fill="var(--gold)">
    <ellipse cx="18" cy="8" rx="13" ry="5"/><path d="M5 12c0 3 6 5 13 5s13-2 13-5v6c0 3-6 5-13 5S5 21 5 18z"/><path d="M5 22c0 3 6 5 13 5s13-2 13-5v6c0 3-6 5-13 5S5 31 5 28z"/><circle cx="35" cy="34" r="7" fill="none" stroke="var(--gold)" stroke-width="3"/>
  </svg>

  <div class="feature left" style="left:26px;top:388px">
    <h3>Intelligent Match</h3>
    <p>Personal finance preference, such<br>as growth or income</p>
  </div>
  <svg class="feature-icon" style="left:350px;top:386px" viewBox="0 0 44 44" fill="none" stroke="var(--gold)" stroke-width="3">
    <rect x="4" y="6" width="36" height="28"/><polyline points="9,27 17,18 23,23 34,12"/><line x1="22" y1="34" x2="22" y2="41"/>
  </svg>

  <div class="emblem" role="img" aria-label="Brand emblem"></div>

  <svg class="feature-icon" style="left:820px;top:253px" viewBox="0 0 44 44" fill="none" stroke="var(--gold)" stroke-width="3">
    <circle cx="22" cy="25" r="15"/><line x1="22" y1="25" x2="22" y2="16"/><line x1="18" y1="5" x2="26" y2="5"/>
  </svg>
  <div class="feature" style="left:881px;top:255px">
    <h3>Sell Faster</h3>
    <p>Sell your property as a performing<br>asset to investors nationwide</p>
  </div>

  <svg class="feature-icon" style="left:820px;top:386px" viewBox="0 0 44 44" fill="var(--gold)">
    <path d="M22 5 4 20h5v19h12V28h6v11h8V20h5z"/>
  </svg>
  <div class="feature" style="left:881px;top:388px">
    <h3>Keep Tenants</h3>
    <p>You can sell without having to wait<br>until property isvacant</p>
  </div>
</section>

<section class="listings">
  <h2 class="section-title serif" style="top:52px">New Listings</h2>
  <p class="listings-link">View all 360 Listings</p>

  <article class="listing" style="left:30px">
    <div class="listing-photo" role="img" aria-label="Contemporary home with pool and outdoor lounge" style="background:linear-gradient(180deg,#3f8fd8 0%,#8fc2ea 35%,#c08a5a 60%,#2f9ec6 85%,#6b8d7a 100%)"></div>
    <div class="listing-meta"><div class="specs"><span>2 bed</span><span>2 bath</span></div>12 Elm Row Unit 3, Oldbury, 40213<br>West Midlands</div>
  </article>
  <article class="listing" style="left:318px">
    <div class="listing-photo" role="img" aria-label="White and black modern two storey house with garage" style="background:linear-gradient(180deg,#9dbbd8 0%,#e8e8e6 35%,#3a3b3e 60%,#d6d6d3 85%,#8a8a86 100%)"></div>
    <div class="listing-meta"><div class="specs"><span>2 bed</span><span>2 bath</span></div>12 Elm Row Unit 3, Oldbury, 40213<br>West Midlands</div>
  </article>
  <article class="listing" style="left:607px">
    <div class="listing-photo" role="img" aria-label="Stone and timber modern house at twilight" style="background:linear-gradient(180deg,#4d6b94 0%,#8f9aa8 35%,#6d5a4c 60%,#c7b9a6 85%,#5b5e55 100%)"></div>
    <div class="listing-meta"><div class="specs"><span>2 bed</span><span>2 bath</span></div>12 Elm Row Unit 3, Oldbury, 40213<br>West Midlands</div>
  </article>
  <article class="listing" style="left:894px">
    <div class="listing-photo" role="img" aria-label="Glass fronted modern house lit up at night" style="background:linear-gradient(180deg,#2a7fd0 0%,#5aa3e0 35%,#3c4a58 60%,#d9a25a 75%,#2b3640 100%)"></div>
    <div class="listing-meta"><div class="specs"><span>2 bed</span><span>2 bath</span></div>12 Elm Row Unit 3, Oldbury, 40213<br>West Midlands</div>
  </article>
</section>

<section class="stats">
  <div class="stat" style="left:230px"><b>500</b><span>Homes for sale</span></div>
  <div class="stat" style="left:489px"><b>276</b><span>Recently sold</span></div>
  <div class="stat" style="left:709px"><b>1</b><span>Foreclosure</span></div>
  <div class="stat" style="left:921px"><b>86</b><span>Price reduced</span></div>
</section>

<section class="sell">
  <div class="feature-photo" role="img" aria-label="Modern house with stone and timber facade at sunset"></div>
  <h2 class="block-title serif" style="left:660px;top:60px">Sell</h2>
  <div class="block-copy" style="left:662px;top:155px">
    <p>We undertake the necessary market research to evaluate an option that works for all parties involved. We will help guide you to make an informed decision on how to gain the maximum realistic value</p>
    <p>For those looking to achieve a fast and professional sale to experienced investors, we provide an approach that has been proven to work for many others</p>
    <p>If you would like to discuss a property you are looking to sell, then please contact us on 01632 960418</p>
  </div>
  <div class="btn" style="left:662px;top:377px">Learn More</div>
</section>

<section class="invest">
  <h2 class="block-title serif" style="left:57px;top:57px">Invest</h2>
  <div class="block-copy" style="left:59px;top:140px;width:490px">
    <p>We have our own portfolio and we are active investors, so our finger is on the pulse and we are currently looking for residential development investments &amp; commercial to residential conversions in cities or regional centres showing strong growth</p>
    <p>Our experience in the industry enables us to make extremely quick and well-informed decisions. We follow the opportunities that are presented to us as well as sourcing opportunities ourselves. We are happy to work in partnership and within joint ventures and have a proven track record of establishing excellent relationships in these areas.</p>
  </div>
  <div class="btn" style="left:59px;top:370px">Learn More</div>
  <div class="feature-photo" role="img" aria-label="Snow covered timber cabin lit at dusk beside a lake with pine trees"></div>
</section>

<section class="contact">
  <h2 class="contact-heading">Contact us on<br>01632 960418</h2>
  <div class="contact-rule"></div>
  <p class="contact-region">West Midlands, United Kingdom</p>
  <p class="contact-address">27 Foundry Lane Suite 5<br>UK</p>
  <div class="info-col" style="left:94px">
    <h4>Get in touch</h4>
    <div>Website: <span class="soft">Blah blah</span></div>
    <div>Phone: <span class="soft">Blah blah</span></div>
    <div>Email: <span class="soft">Blah blah</span></div>
  </div>
  <div class="info-col" style="left:306px">
    <h4>Sitemap</h4>
    <div class="soft">Blah blah</div>
    <div class="soft">Blah blah</div>
    <div class="soft">Blah blah</div>
  </div>
  <div class="map" role="img" aria-label="Circular street map of the West Midlands region"></div>
</section>

</body>
</html>
```